Commercial facility maintenance

I need a card design that helps my salesmen make contact with new clients, our product is facility maintenance and heavy industrial maintenance

```html
<!DOCTYPE html>
<html lang="en">
<head>
<meta charset="utf-8">
<title>Harlow Millworks LLC – Business Card</title>
<link href="https://fonts.googleapis.com/css2?family=Poppins:ital,wght@0,400;0,500;0,600;0,700;1,400;1,500&display=swap" rel="stylesheet">
<style>
  :root {
    --page-bg: #c7cfd7;
    --card-bg: #ffffff;
    --brand-red: #8f1419;
    --brand-red-edge: #d61f26;
    --charcoal: #33373a;
    --charcoal-edge: #8a8d92;
    --ink: #2f3236;
    --photo-top: #d9c7b8;
    --photo-mid: #b9babd;
    --photo-bottom: #7f8185;
  }
  * { box-sizing: border-box; margin: 0; padding: 0; }
  html, body { width: 923px; height: 1200px; overflow: hidden; }
  body {
    background: var(--page-bg);
    font-family: "Poppins", sans-serif;
    position: relative;
  }
  .card {
    position: absolute;
    left: 62px;
    width: 798px;
    height: 456px;
    background: linear-gradient(180deg, #fbfbfb 0%, var(--card-bg) 60%);
    overflow: hidden;
  }
  .card--front { top: 97px; }
  .card--back {
    top: 600px;
    border-right: 2px solid var(--brand-red-edge);
  }

  /* Front */
  .brand {
    position: absolute;
    top: 110px;
    left: 0;
    width: 100%;
    display: flex;
    justify-content: center;
    align-items: center;
    gap: 14px;
  }
  .brand__mark {
    width: 96px;
    height: 96px;
    border-radius: 50%;
    background: var(--brand-red);
    flex: none;
  }
  .brand__name {
    font-weight: 700;
    font-size: 34px;
    color: var(--charcoal);
    letter-spacing: 0.5px;
  }
  .service-pill {
    position: absolute;
    left: 115px;
    width: 568px;
    height: 55px;
    border-radius: 28px;
    display: flex;
    align-items: center;
    justify-content: center;
    color: #fff;
    font-weight: 600;
    font-size: 20px;
    letter-spacing: 3.4px;
  }
  .service-pill--commercial {
    top: 275px;
    background: var(--brand-red);
    border: 2px solid var(--brand-red-edge);
  }
  .service-pill--industrial {
    top: 340px;
    background: var(--charcoal);
    border: 2px solid var(--charcoal-edge);
  }

  /* Back */
  .portrait {
    position: absolute;
    left: 0;
    top: 14px;
    width: 384px;
    height: 442px;
    background: linear-gradient(180deg, var(--photo-top) 0%, var(--photo-mid) 50%, var(--photo-bottom) 100%);
    clip-path: polygon(0 442px, 0 270px, 95px 225px, 95px 60px, 120px 18px, 210px 10px, 250px 50px, 255px 230px, 345px 285px, 384px 442px);
  }
  .bottom-rule {
    position: absolute;
    left: 384px;
    right: 0;
    bottom: 0;
    height: 2px;
    background: var(--brand-red-edge);
  }
  .name-pill {
    position: absolute;
    left: 285px;
    top: 86px;
    width: 415px;
    height: 62px;
    border-radius: 32px;
    background: var(--brand-red);
    border: 2px solid var(--brand-red-edge);
    display: flex;
    align-items: center;
    justify-content: center;
    color: #fff;
    font-size: 30px;
    font-weight: 400;
  }
  .name-pill strong { font-weight: 700; margin-right: 8px; }
  .job-title {
    position: absolute;
    left: 287px;
    top: 158px;
    font-style: italic;
    font-weight: 500;
    font-size: 18px;
    line-height: 23px;
    color: var(--ink);
  }
  .divider {
    position: absolute;
    left: 290px;
    top: 228px;
    width: 458px;
    border-top: 1.5px dashed var(--brand-red-edge);
  }
  .contact-list { list-style: none; }
  .contact-item {
    position: absolute;
    left: 387px;
    display: flex;
    align-items: center;
    gap: 18px;
    font-size: 18px;
    color: var(--ink);
  }
  .contact-item svg { width: 20px; height: 20px; flex: none; }
  .contact-item--phone { top: 286px; }
  .contact-item--email { top: 333px; }
  .contact-item--web { top: 379px; }
</style>
</head>
<body>

<section class="card card--front">
  <div class="brand">
    <span class="brand__mark"></span>
    <span class="brand__name">Harlow Millworks LLC</span>
  </div>
  <div class="service-pill service-pill--commercial">COMMERCIAL FACILITY MAINTENANCE</div>
  <div class="service-pill service-pill--industrial">HEAVY INDUSTRIAL MAINTENANCE</div>
</section>

<section class="card card--back">
  <div class="portrait" role="img" aria-label="Portrait photo of the team member in a grey suit and dark tie"></div>
  <div class="bottom-rule"></div>

  <div class="name-pill"><strong>DANIEL</strong>ROURKE</div>
  <p class="job-title">Specialist,<br>Heavy industrial maintenance</p>
  <div class="divider"></div>

  <ul class="contact-list">
    <li class="contact-item contact-item--phone">
      <svg viewBox="0 0 24 24" aria-hidden="true"><path fill="#d61f26" d="M6.6 10.8a15.1 15.1 0 0 0 6.6 6.6l2.2-2.2c.3-.3.7-.4 1-.2 1.1.4 2.3.6 3.6.6.6 0 1 .4 1 1V20c0 .6-.4 1-1 1A17 17 0 0 1 3 4c0-.6.4-1 1-1h3.5c.6 0 1 .4 1 1 0 1.3.2 2.5.6 3.6.1.3 0 .7-.2 1z"/></svg>
      <span>555-014-2290</span>
    </li>
    <li class="contact-item contact-item--email">
      <svg viewBox="0 0 24 24" aria-hidden="true"><rect x="2" y="5" width="20" height="14" fill="#d61f26"/><path d="M2 5l10 8 10-8M2 19l7-6M22 19l-7-6" stroke="#fff" stroke-width="1.5" fill="none"/></svg>
      <span>daniel@harlowmillworksllc.com</span>
    </li>
    <li class="contact-item contact-item--web">
      <svg viewBox="0 0 24 24" aria-hidden="true"><circle cx="12" cy="12" r="10" fill="#d61f26"/><path d="M2 12h20M12 2v20M4 7h16M4 17h16M12 2c-4 4-4 16 0 20M12 2c4 4 4 16 0 20" stroke="#fff" stroke-width="1.3" fill="none"/></svg>
      <span>www.harlowmillworksllc.com</span>
    </li>
  </ul>
</section>

</body>
</html>
```